" Sou uma médica cirurgiã plástica que atendendo numa clínica (que não é própria), fazendo parte de uma equipe de cirurgiões plásticos mais experientes que atende pacientes classe A em São Paulo. Faço todos os tipos de cirurgia plástica, mas tenho uma maior foco nas cirurgias de face (bleroplastia, ritidoplastia), mamoplastia e transplante capilar, além de procedimentos (laser, preenchedores/harmonização facial, dravix). "

```html
<!DOCTYPE html>
<html lang="pt-BR">
<head>
<meta charset="utf-8">
<title>Dra. Marina Duarte — Cartão de visita</title>
<link rel="stylesheet" href="https://fonts.googleapis.com/css2?family=Cinzel:wght@400&family=Montserrat:wght@400;500&display=swap">
<style>
  :root {
    --plum: #8b1c62;
    --plum-deep: #7a1656;
    --rose: #d98aad;
    --rose-band: #d67fa6;
    --paper: #ffffff;
    --stage: #ebeae8;
    --ink: #5a1342;
  }
  * { box-sizing: border-box; margin: 0; padding: 0; }
  html, body { width: 1200px; height: 1200px; overflow: hidden; }
  body {
    background: var(--stage);
    position: relative;
    font-family: "Montserrat", sans-serif;
    color: var(--plum);
  }
  .card {
    position: absolute;
    overflow: hidden;
    border-radius: 30px;
    box-shadow: 0 6px 18px rgba(0,0,0,0.18);
  }

  /* Front */
  .card-front {
    left: 336px; top: 187px; width: 547px; height: 377px;
    background: var(--paper);
  }
  .band { position: absolute; top: 36px; bottom: 36px; width: 28px; }
  .band-left { left: 0; background: var(--plum); }
  .band-right { right: 0; background: var(--rose-band); }
  .front-lockup {
    position: absolute; left: 30px; width: 440px; top: 82px;
    text-align: center;
  }
  .mark-square {
    display: inline-block; width: 108px; height: 108px;
    border: 6px solid var(--plum);
  }
  .brand-name {
    font-family: "Cinzel", serif; font-weight: 400; color: var(--plum);
    line-height: 1;
  }
  .front-lockup .brand-name { margin-top: 16px; font-size: 42px; letter-spacing: 1px; }
  .brand-name .title { font-size: 0.42em; display: block; margin-bottom: 4px; }
  .specialty {
    font-family: "Montserrat", sans-serif; font-weight: 500;
    color: var(--plum); text-transform: uppercase;
  }
  .front-lockup .specialty { margin-top: 8px; font-size: 16px; letter-spacing: 5px; }

  /* Back */
  .card-back {
    left: 317px; top: 636px; width: 614px; height: 396px;
    background: var(--rose);
  }
  .back-lockup {
    position: absolute; left: 48px; top: 55px;
    display: flex; align-items: center; gap: 16px;
  }
  .back-lockup .mark-square { width: 84px; height: 84px; border-width: 5px; }
  .back-lockup .brand-name { font-size: 36px; letter-spacing: 1px; }
  .back-lockup .specialty { margin-top: 6px; font-size: 14px; letter-spacing: 4.5px; padding-left: 40px; }
  .deco-square {
    position: absolute; left: 422px; top: 137px; width: 230px; height: 215px;
    border: 7px solid var(--plum);
  }
  .contact { position: absolute; left: 60px; top: 190px; list-style: none; }
  .contact li {
    display: flex; align-items: flex-start; gap: 14px;
    font-size: 17px; color: var(--ink); line-height: 26px;
  }
  .contact li.address { margin-top: 30px; line-height: 28px; }
  .contact svg { flex: none; margin-top: 5px; }
  .dot { width: 14px; height: 14px; border-radius: 50%; background: var(--ink); margin: 6px 2px 0; flex: none; }
</style>
</head>
<body>
  <section class="card card-front" aria-label="Frente do cartão">
    <div class="band band-left"></div>
    <div class="band band-right"></div>
    <div class="front-lockup">
      <span class="mark-square"></span>
      <p class="brand-name"><span class="title">Dra.</span>Marina Duarte</p>
      <p class="specialty">Cirurgiã Plástica</p>
    </div>
  </section>

  <section class="card card-back" aria-label="Verso do cartão">
    <div class="deco-square"></div>
    <div class="back-lockup">
      <span class="mark-square"></span>
      <div>
        <p class="brand-name"><span class="title">Dra.</span>Marina Duarte</p>
        <p class="specialty">Cirurgiã Plástica</p>
      </div>
    </div>
    <ul class="contact">
      <li>
        <svg width="18" height="18" viewBox="0 0 24 24" aria-hidden="true"><path fill="#5a1342" d="M6.6 10.8a15.1 15.1 0 0 0 6.6 6.6l2.2-2.2a1 1 0 0 1 1-.25 11.4 11.4 0 0 0 3.6.57 1 1 0 0 1 1 1V20a1 1 0 0 1-1 1A17 17 0 0 1 3 4a1 1 0 0 1 1-1h3.5a1 1 0 0 1 1 1c0 1.25.2 2.45.57 3.57a1 1 0 0 1-.25 1z"/></svg>
        (11) 5048-2719
      </li>
      <li><span class="dot"></span>(11) 94831-207</li>
      <li class="address">
        <svg width="18" height="22" viewBox="0 0 24 30" aria-hidden="true"><path fill="#5a1342" d="M12 0C5.4 0 0 5.3 0 11.8 0 20.7 12 30 12 30s12-9.3 12-18.2C24 5.3 18.6 0 12 0zm0 16.5a4.8 4.8 0 1 1 0-9.6 4.8 4.8 0 0 1 0 9.6z"/></svg>
        <span>Alameda das Acácias nº212<br>Moema, São Paulo.</span>
      </li>
    </ul>
  </section>
</body>
</html>
```